Realty Group Needs Classy, Contemporary Letterhead Design

We need a letterhead design for a new realty company located in NY, USA. We buy investment properties to rehabilitate and or keep in our rental portfolio.

```html
<!DOCTYPE html>
<html lang="en">
<head>
<meta charset="utf-8">
<title>Meridian Realty Group – Letterhead</title>
<link rel="stylesheet" href="https://fonts.googleapis.com/css2?family=Lato:wght@400;700&family=Open+Sans:wght@400&display=swap">
<style>
  :root {
    --brand-purple: #4f2a8a;
    --ink: #1d1d1d;
    --body-ink: #4a4a4a;
    --paper: #ffffff;
    --backdrop: #e6e6e9;
  }
  * { box-sizing: border-box; margin: 0; padding: 0; }
  html, body {
    width: 1040px; height: 1200px; overflow: hidden;
    background: var(--backdrop);
  }
  .letterhead {
    position: absolute; left: 77px; top: 30px;
    width: 886px; height: 1140px;
    background: var(--paper);
    box-shadow: 0 2px 10px rgba(0,0,0,.15);
    overflow: hidden;
    font-family: "Open Sans", sans-serif;
    color: var(--body-ink);
  }
  .brand {
    position: absolute; left: 83px; top: 44px;
    display: flex; align-items: center; gap: 9px;
    font-family: "Lato", sans-serif; font-weight: 700;
    font-size: 23px; line-height: 28px; color: var(--brand-purple);
  }
  .brand-dot {
    width: 13px; height: 13px; border-radius: 50%;
    background: var(--brand-purple);
  }
  .contact {
    position: absolute; right: 84px; top: 38px;
    list-style: none; text-align: right;
    font-family: "Lato", sans-serif; font-size: 17px; color: var(--ink);
    line-height: 21px;
  }
  .contact li { display: flex; justify-content: flex-end; align-items: center; gap: 8px; }
  .icon { width: 16px; height: 16px; fill: var(--brand-purple); flex: none; }
  .letter-body {
    position: absolute; left: 83px; top: 222px; width: 716px;
    font-size: 14.5px; line-height: 25.5px;
  }
  .issue-date { margin-bottom: 10px; }
  .recipient { line-height: 17px; margin-bottom: 46px; }
  .salutation { margin-bottom: 22px; }
  .paragraph { margin-bottom: 25px; text-align: justify; hyphens: auto; -webkit-hyphens: auto; }
  .closing { margin-top: 44px; }
  .signature {
    width: 205px; height: 24px; margin: 8px 0 8px;
    background: linear-gradient(90deg, rgba(60,60,60,.22), rgba(60,60,60,.06));
    border-radius: 3px;
  }
  .signer-name { font-size: 17px; color: var(--ink); line-height: 24px; }
  .signer-role { font-size: 14.5px; }
  .footer-art {
    position: absolute; left: 0; bottom: 0; width: 345px; height: 228px;
    background: radial-gradient(ellipse at 20% 100%, var(--brand-purple) 0%, rgba(79,42,138,.7) 45%, rgba(79,42,138,0) 75%);
  }
  .address {
    position: absolute; right: 84px; bottom: 34px;
    display: flex; align-items: center; gap: 8px;
    font-family: "Lato", sans-serif; font-size: 17px; color: var(--ink);
  }
  .address .icon { width: 18px; height: 24px; }
</style>
</head>
<body>
<main class="letterhead" lang="en">
  <header>
    <div class="brand"><span class="brand-dot"></span>Meridian Realty Group, LLC</div>
    <ul class="contact">
      <li>044-987 654 321
        <svg class="icon" viewBox="0 0 16 16"><path d="M2 5c0-2 3-3 6-3s6 1 6 3v1h-3V5H5v1H2z M4 7h8l2 6H2z"/></svg></li>
      <li>info@meridianrg.com
        <svg class="icon" viewBox="0 0 16 16"><path d="M1 3h14v10H1z M2 4l6 5 6-5" fill="var(--brand-purple)" stroke="#fff" stroke-width="1"/></svg></li>
      <li>www.meridianrg.com
        <svg class="icon" viewBox="0 0 16 16"><circle cx="8" cy="8" r="7"/><path d="M4 6h4v3H5z M9 9h3v3H9z" fill="#fff"/></svg></li>
    </ul>
  </header>

  <section class="letter-body">
    <p class="issue-date">Issuing Date: May 5, 2018</p>
    <p class="recipient">Name Of Employee Mr. XYZABC<br>Address of Employee<br>Address Line 2 etc..</p>
    <p class="salutation">Dear Mr.XYZABC</p>
    <p class="paragraph">Lorem Ipsum has been the industry's standard dummy text ever since the 1500s, when an unknown printer took a galley of type and scrambled it to make a type specimen book. It has survived not only five centuries, but also the leap into electronic typesetting, remaining essentially unchanged. It was popularised in the 1960s with the release of Letraset sheets containing Lorem Ipsum passages, and more recently with desktop publishing software like Aldus PageMaker including versions of Lorem Ipsum.</p>
    <p class="paragraph">Lorem Ipsum is simply dummy text of the printing and typesetting industry. Lorem Ipsum has been the industry's standard dummy text ever since the 1500s, when an unknown printer took a galley of type and scrambled it to make a type specimen book.</p>
    <p class="paragraph">It has survived not only five centuries, but also the leap into electronic typesetting, remaining essentially unchanged. It was popularised in the 1960s with the release of Letraset sheets containing Lorem IpsumIpsum passages.</p>
    <p class="closing">Yours Sincerely</p>
    <div class="signature" role="img" aria-label="Handwritten signature of Daniel Whitmore"></div>
    <p class="signer-name">Daniel Whitmore</p>
    <p class="signer-role">Managing Director</p>
  </section>

  <div class="footer-art" role="img" aria-label="Purple silhouette illustration of an archer drawing a bow"></div>

  <footer class="address">88, Harbor Street Albany, New York, 12207
    <svg class="icon" viewBox="0 0 18 24"><path d="M9 0a8 8 0 0 0-8 8c0 6 8 16 8 16s8-10 8-16a8 8 0 0 0-8-8z"/><circle cx="9" cy="8" r="3" fill="#fff"/></svg>
  </footer>
</main>
</body>
</html>
```